Bath Salt - Sachet Packet (5 Scents) Packaging Design

We sell products to professional salons in the USA. This product is used as the first step when treating clients to a pedicure spa. This product is called SALT SOAK (or Bath Salts). The salt is added to the water to cleanse the skin, create a pleasant fragrance, and change the color of the water.

This product has 5 different variations, based on the scent of the salt soak. The available scents are:
LAVENDER, MANDARIN, CUCUMBER-MELON, JASMINE, MINT.

We would like to see package designs for all 5 scents. The theme should be consistent across the different variations of scents. The design should focus on bright, attractive, floral colors/themes. The design should fully express the color and imagery that are associated with each scent. (Lavender scent should include purple colors, lavender flower, etc.). See example images for reference of popular designs/brands.

Ideal designs will incorporate a luxurious and premium aesthetic that combines elegant imagery, colors, and premium finishes. See example images for reference of popular designs/brands.

Each packet is individually sealed. See dimension artwork file for reference of the sachet packet size and layout.

See the attached document guidelines for more information about product name, key text, and brand logo.

Target Market(s)

Beauty & Nail Salons

Industry/Entity Type

Beauty

Font styles to use
Sans Serif
Script

Requirements
Must have
• Bright imagery and colors that relate to the target fragrance
Nice to have
• Premium and luxurious finishes (shiny accent, etc.)

```html
<!DOCTYPE html>
<html lang="en">
<head>
<meta charset="utf-8">
<title>VELA Salt Soak – Mint</title>
<link href="https://fonts.googleapis.com/css2?family=Cinzel:wght@600&family=Great+Vibes&family=Montserrat:wght@400;600&display=swap" rel="stylesheet">
<style>
  :root {
    --page: #ffffff;
    --pouch: #a8ecdf;
    --pouch-edge: #95e2d3;
    --label: #86eed8;
    --gold: #d9ad3c;
    --gold-light: #f6dc86;
    --ink: #1f2b2a;
    --teal: #2f9c82;
    --rule: #2f9c86;
    --leaf-a: #7ccf4a;
    --leaf-b: #2f8a3a;
    --small: #6fb8a6;
  }
  * { margin: 0; padding: 0; box-sizing: border-box; }
  html, body { width: 1110px; height: 1200px; overflow: hidden; background: var(--page); }
  .canvas { position: relative; width: 1110px; height: 1200px; }

  .pouch {
    position: absolute; left: 175px; top: 90px; width: 760px; height: 1020px;
    background: linear-gradient(180deg, #b4efe4 0%, var(--pouch) 60%, #9fe8d9 100%);
    border-radius: 14px;
  }
  .zip-line {
    position: absolute; left: 10px; right: 10px; height: 2px;
    background: var(--pouch-edge);
  }
  .zip-line.upper { top: 79px; }
  .zip-line.lower { top: 112px; }

  .label-frame { position: absolute; left: 280px; top: 267px; width: 557px; height: 753px; }

  .brand {
    position: absolute; left: 0; right: 0; top: 322px; text-align: center;
    font-family: "Montserrat", sans-serif; font-weight: 600; font-size: 44px;
    letter-spacing: 2px; color: var(--ink);
  }
  .product-name {
    position: absolute; left: 0; right: 0; top: 420px; text-align: center;
    font-family: "Cinzel", serif; font-weight: 600; font-size: 82px; letter-spacing: 1px;
    background: linear-gradient(180deg, var(--gold-light) 0%, var(--gold) 55%, #b88a22 100%);
    -webkit-background-clip: text; background-clip: text; color: transparent;
  }
  .scent {
    position: absolute; left: 0; right: 0; top: 528px; text-align: center;
    font-family: "Great Vibes", cursive; font-size: 76px; color: var(--teal);
  }
  .scent-art {
    position: absolute; left: 432px; top: 628px; width: 255px; height: 180px;
    border-radius: 50% 45% 50% 40%;
    background: radial-gradient(ellipse at 45% 45%, var(--leaf-a) 0%, var(--leaf-b) 75%, transparent 76%);
  }
  .divider {
    position: absolute; left: 313px; width: 481px; top: 752px; height: 2px; background: var(--rule);
  }
  .seal {
    position: absolute; left: 505px; top: 852px; width: 100px; height: 100px;
    border-radius: 50%; border: 3px solid #ffffff; background: rgba(255,255,255,0.15);
  }
  .net-weight {
    position: absolute; left: 0; right: 0; top: 962px; text-align: center;
    font-family: "Montserrat", sans-serif; font-weight: 400; font-size: 16px;
    letter-spacing: 0.5px; color: var(--small);
  }
</style>
</head>
<body>
<main class="canvas">
  <div class="pouch">
    <span class="zip-line upper"></span>
    <span class="zip-line lower"></span>
  </div>

  <svg class="label-frame" viewBox="0 0 557 753" aria-hidden="true">
    <path d="M60 70 Q278 -10 497 70 L497 100 L540 100 L540 653 L497 653 L497 683 Q278 763 60 683 L60 653 L17 653 L17 100 L60 100 Z"
          fill="var(--label)" stroke="var(--gold)" stroke-width="4"/>
    <path d="M72 80 Q278 8 485 80 L485 112 L528 112 L528 641 L485 641 L485 673 Q278 745 72 673 L72 641 L29 641 L29 112 L72 112 Z"
          fill="none" stroke="var(--gold-light)" stroke-width="1.5"/>
  </svg>

  <div class="brand">VELA</div>
  <h1 class="product-name">SALT SOAK</h1>
  <div class="scent">Mint</div>
  <div class="scent-art" role="img" aria-label="Fresh green mint leaves"></div>
  <div class="divider"></div>
  <div class="seal" role="img" aria-label="Organic certification seal"></div>
  <div class="net-weight">100g NT WGT</div>
</main>
</body>
</html>
```